Criação de Papelaria (6 itens) para Vértice & Aurora
" Funciona como dedetizadora como foco principal, possuindo a divisão dedetizadora ( controladora de pragas urbanas), a divisão hospitalar ( Comercio de equipamentos médico hospitalar), a divisão Higienização ( comércio de produtos de higiene e limpeza). O foco principal é a dedetizadora. "

```html
<!DOCTYPE html>
<html lang="pt-BR">
<head>
<meta charset="utf-8">
<title>Vértice &amp; Aurora — Cartão de visita</title>
<link rel="stylesheet" href="https://fonts.googleapis.com/css2?family=Roboto:wght@400;500;900&display=swap">
<style>
  :root {
    --bg: #e9e9e6;
    --card: #ffffff;
    --ink: #6d6f72;
    --ink-dark: #505256;
    --red: #d0161d;
    --red-dark: #9c0f14;
    --green: #1e6b3a;
  }
  * { box-sizing: border-box; margin: 0; padding: 0; }
  html, body { width: 1200px; height: 1200px; overflow: hidden; }
  body {
    background: var(--bg);
    font-family: "Roboto", Arial, sans-serif;
    display: flex; align-items: center; justify-content: center;
  }
  .business-card {
    position: relative;
    width: 880px; height: 880px;
    background: var(--card);
    border-radius: 44px;
    overflow: hidden;
    box-shadow: 0 10px 30px rgba(0,0,0,.12);
  }
  .brand {
    position: absolute; top: 170px; left: 0; right: 0;
    display: flex; flex-direction: column; align-items: center;
  }
  .brand-row { display: flex; align-items: center; gap: 26px; }
  .brand-mark {
    width: 96px; height: 96px; border-radius: 50%;
    background: var(--red);
  }
  .brand-name {
    font-weight: 900; font-size: 84px; letter-spacing: -1px;
    color: var(--ink-dark); line-height: 1;
  }
  .brand-tagline {
    margin-top: 18px;
    font-weight: 500; font-size: 34px; letter-spacing: 16px;
    color: var(--red); text-transform: uppercase;
  }
  .contacts {
    position: absolute; top: 560px; left: 60px; right: 60px;
    display: grid; grid-template-columns: 1fr 1fr; column-gap: 40px; row-gap: 34px;
    font-size: 27px; color: var(--ink);
  }
  .contact { display: flex; align-items: center; gap: 16px; white-space: nowrap; }
  .contact svg { width: 30px; height: 30px; flex: none; fill: var(--red); }
  .contacts .web { grid-column: 1; grid-row: 1; }
  .contacts .address { grid-column: 1; grid-row: 2; }
  .contacts .phone { grid-column: 2; grid-row: 2; }
  .contacts .email { grid-column: 2; grid-row: 3; font-size: 25px; }
  .bottom-band { position: absolute; left: 0; bottom: 0; width: 880px; height: 180px; }
</style>
</head>
<body>
  <article class="business-card">
    <header class="brand">
      <div class="brand-row">
        <span class="brand-mark"></span>
        <h1 class="brand-name">Vértice &amp; Aurora</h1>
      </div>
      <p class="brand-tagline">Dedetizadora</p>
    </header>

    <section class="contacts">
      <p class="contact web">
        <svg viewBox="0 0 24 24"><circle cx="12" cy="12" r="10" fill="none" stroke="#d0161d" stroke-width="2"/><path d="M2 12h20M12 2c3 3 3 17 0 20M12 2c-3 3-3 17 0 20" fill="none" stroke="#d0161d" stroke-width="1.6"/></svg>
        www.verticeaurora.com.br
      </p>
      <p class="contact address">
        <svg viewBox="0 0 24 24"><path d="M12 2a7 7 0 0 0-7 7c0 5 7 13 7 13s7-8 7-13a7 7 0 0 0-7-7zm0 9.5A2.5 2.5 0 1 1 12 6.5a2.5 2.5 0 0 1 0 5z"/></svg>
        Rua das Acácias, 00 Centro
      </p>
      <p class="contact phone">
        <svg viewBox="0 0 24 24"><path d="M6.6 10.8a15 15 0 0 0 6.6 6.6l2.2-2.2a1 1 0 0 1 1-.25 11 11 0 0 0 3.6.6 1 1 0 0 1 1 1V20a1 1 0 0 1-1 1A17 17 0 0 1 3 4a1 1 0 0 1 1-1h3.5a1 1 0 0 1 1 1 11 11 0 0 0 .6 3.6 1 1 0 0 1-.25 1z"/></svg>
        (11) 0000-0000
      </p>
      <p class="contact email">
        <svg viewBox="0 0 24 24"><path d="M3 5h18a1 1 0 0 1 1 1v12a1 1 0 0 1-1 1H3a1 1 0 0 1-1-1V6a1 1 0 0 1 1-1zm9 7.5L20 7H4z"/></svg>
        contato@verticeaurora.com.br
      </p>
    </section>

    <svg class="bottom-band" viewBox="0 0 880 180" preserveAspectRatio="none" aria-hidden="true">
      <path d="M0 40 C 200 150, 560 175, 880 160 L880 180 L0 180 Z" fill="#1e6b3a"/>
      <path d="M0 62 C 200 165, 560 185, 880 172 L880 180 L0 180 Z" fill="#d0161d"/>
      <path d="M0 120 C 160 175, 360 182, 520 180 L0 180 Z" fill="#9c0f14"/>
    </svg>
  </article>
</body>
</html>
```